Clean and modern business cards

Looking for an updated business card design for my dental office “corvanta dental” . Looking for a modern clean / sleek design . I’m thinking black background but open to seeing other options . One side needs to have an appointment card . Card needs to have logo, dentist name , phone, email , address . I’ve attached couple of cards I thought were cool as well as my logo
Target Market(s)
Dental patients
Industry/Entity Type
Dentistry
Contact Information for Business Card
Phone email address

```html
<!DOCTYPE html>
<html lang="en">
<head>
<meta charset="utf-8">
<title>Corvanta Dental – Business Cards</title>
<link href="https://fonts.googleapis.com/css2?family=Montserrat:wght@400;500;600;700&display=swap" rel="stylesheet">
<style>
  :root {
    --backdrop: #c8c8c8;
    --card-light: #ffffff;
    --card-light-edge: #ececec;
    --card-dark: #1e1e1e;
    --ink: #1a1a1a;
    --rule: #777777;
    --on-dark: #e8e8e8;
    --on-dark-soft: #bdbdbd;
    --accent: #f2b632;
  }
  * { box-sizing: border-box; margin: 0; padding: 0; }
  html, body { width: 1084px; height: 1200px; overflow: hidden; }
  body {
    background: var(--backdrop);
    font-family: "Montserrat", sans-serif;
    display: flex;
    flex-direction: column;
    align-items: center;
    justify-content: center;
    gap: 60px;
  }
  .card {
    width: 880px;
    height: 503px;
    position: relative;
    box-shadow: 0 4px 10px rgba(0,0,0,0.28);
    overflow: hidden;
  }

  /* Appointment side */
  .appointment-card {
    background: linear-gradient(115deg, var(--card-light-edge) 0%, var(--card-light) 70%);
    color: var(--ink);
    text-align: center;
  }
  .brand-watermark {
    position: absolute;
    left: -74px;
    top: -8px;
    width: 500px;
    height: 500px;
    border-radius: 50%;
    background: radial-gradient(circle, rgba(200,210,235,0.28) 0%, rgba(230,220,200,0.22) 55%, rgba(220,220,220,0.12) 75%, rgba(255,255,255,0) 76%);
  }
  .appointment-content {
    position: relative;
    padding-top: 50px;
    margin-left: 0;
    width: 880px;
    display: flex;
    flex-direction: column;
    align-items: center;
  }
  .appointment-title {
    font-size: 32px;
    font-weight: 500;
    margin-left: 0;
    transform: translateX(-130px);
  }
  .field {
    width: 312px;
    border-top: 1.5px solid var(--rule);
    font-size: 19px;
    padding-top: 8px;
    transform: translateX(-130px);
  }
  .field-date { margin-top: 64px; }
  .field-time { margin-top: 44px; }
  .policy-note {
    margin-top: 44px;
    font-size: 22px;
    font-weight: 500;
    line-height: 1.3;
    transform: translateX(-130px);
  }
  .practice-details {
    margin-top: 42px;
    font-size: 16px;
    line-height: 1.55;
    text-transform: uppercase;
    transform: translateX(-130px);
  }

  /* Identity side */
  .identity-card {
    background: var(--card-dark);
    color: var(--on-dark);
    text-align: center;
  }
  .brand-lockup {
    position: absolute;
    top: 82px;
    left: 0;
    right: 0;
    display: flex;
    align-items: center;
    justify-content: center;
    gap: 18px;
  }
  .brand-dot {
    width: 70px;
    height: 70px;
    border-radius: 50%;
    background: var(--accent);
  }
  .brand-name {
    font-size: 36px;
    font-weight: 700;
    color: #ffffff;
    letter-spacing: 1px;
  }
  .dentist-info {
    position: absolute;
    top: 345px;
    left: 0;
    right: 0;
  }
  .dentist-name {
    font-size: 30px;
    font-weight: 500;
    color: var(--on-dark-soft);
  }
  .dentist-contact {
    margin-top: 14px;
    font-size: 19px;
    line-height: 1.8;
    color: var(--on-dark-soft);
  }
</style>
</head>
<body>
  <section class="card appointment-card">
    <div class="brand-watermark" role="img" aria-label="Faint Corvanta Dental brand mark ring"></div>
    <div class="appointment-content">
      <h2 class="appointment-title">Your Next Appointment is:</h2>
      <div class="field field-date">Date</div>
      <div class="field field-time">Time</div>
      <p class="policy-note">To Cancel or reschedule please notify us at least<br>48 hours prior to your scheduled appointment</p>
      <p class="practice-details">2410 Alder Crescent, Winnipeg, MB &nbsp;|&nbsp; (204) 555-0182<br>corvantawpg.ca | contact@corvantawpg.ca</p>
    </div>
  </section>

  <section class="card identity-card">
    <div class="brand-lockup">
      <span class="brand-dot"></span>
      <span class="brand-name">CORVANTA DENTAL</span>
    </div>
    <div class="dentist-info">
      <h1 class="dentist-name">Daniel Reyes, DDS</h1>
      <p class="dentist-contact">(204) 555-0182<br>daniel@corvantadental.com</p>
    </div>
  </section>
</body>
</html>
```